Create a business card

I have a previous design, just need minor update -(1) to update details and address for the front view (2 different addresses). (2) redo source file for the back of the business card as per photo attached

Contact Information for Business Card

(1) to update details and address for the front view (2 different addresses). (2) redo source file for the back of the business card as per photo attached

```html
<!DOCTYPE html>
<html lang="en">
<head>
<meta charset="utf-8">
<title>Dr Mei Lin Tan – Business Cards</title>
<link rel="stylesheet" href="https://fonts.googleapis.com/css2?family=Montserrat:wght@300;400;500&display=swap">
<style>
  :root {
    --backdrop: #a2a3a6;
    --card-white: #ffffff;
    --lavender: #d6c9e4;
    --ink: #3f3f42;
    --ink-soft: #4a4a4e;
    --dots: #8a8a8e;
    --brand-blue: #34389a;
    --brand-purple: #8a3a8f;
  }
  * { margin: 0; padding: 0; box-sizing: border-box; }
  html, body { width: 800px; height: 1200px; overflow: hidden; }
  body {
    background: var(--backdrop);
    font-family: "Montserrat", sans-serif;
    color: var(--ink);
    position: relative;
  }
  .card {
    position: absolute;
    width: 556px;
    height: 333px;
    border-radius: 40px;
    background: var(--card-white);
    overflow: hidden;
  }
  .card--appointments { left: 124px; top: 50px; }
  .card--front-a { left: 124px; top: 425px; }
  .card--front-b { left: 126px; top: 798px; }

  .card--front {
    background: linear-gradient(115deg, var(--card-white) 38%, #efe9f5 62%, var(--lavender) 100%);
  }

  /* Appointments card */
  .appointments__title {
    position: absolute;
    top: 32px;
    width: 100%;
    text-align: center;
    font-size: 28px;
    font-weight: 400;
    letter-spacing: 6px;
    color: #2e2e31;
  }
  .appointments__row {
    position: absolute;
    left: 58px;
    width: 436px;
    display: flex;
    align-items: baseline;
    font-size: 15px;
    font-weight: 400;
    color: var(--ink-soft);
  }
  .appointments__row:nth-of-type(1) { top: 110px; }
  .appointments__row:nth-of-type(2) { top: 158px; }
  .appointments__row:nth-of-type(3) { top: 206px; }
  .appointments__field { white-space: nowrap; }
  .appointments__dots {
    border-bottom: 1px dotted var(--dots);
    height: 1px;
    margin: 0 4px 0 4px;
    align-self: flex-end;
    margin-bottom: 4px;
  }
  .appointments__dots--date { width: 196px; }
  .appointments__dots--time { flex: 1; }
  .appointments__note {
    position: absolute;
    top: 261px;
    width: 100%;
    text-align: center;
    font-size: 14px;
    font-weight: 300;
    line-height: 19px;
    color: var(--ink-soft);
  }

  /* Front cards */
  .brand {
    position: absolute;
    left: 36px;
    top: 176px;
    width: 200px;
    display: flex;
    align-items: center;
    justify-content: center;
    gap: 8px;
  }
  .brand__dot {
    width: 10px; height: 10px;
    border-radius: 50%;
    background: var(--brand-blue);
  }
  .brand__name {
    font-size: 18px;
    font-weight: 500;
    color: var(--brand-blue);
    white-space: nowrap;
  }
  .card__divider {
    position: absolute;
    left: 231px;
    top: 51px;
    width: 1.5px;
    height: 230px;
    background: #3a3a3d;
  }
  .details {
    position: absolute;
    left: 248px;
    top: 44px;
    font-size: 14.5px;
    font-weight: 400;
    line-height: 18.4px;
    color: var(--ink-soft);
  }
  .details__name {
    font-size: 26px;
    font-weight: 500;
    line-height: 32px;
    letter-spacing: -0.6px;
    color: #4a4a4d;
  }
  .details__credentials { line-height: 21px; }
  .details__specialty { line-height: 21px; margin-bottom: 8px; }
  .details__contact { margin-bottom: 9px; }
</style>
</head>
<body>

<section class="card card--appointments">
  <h1 class="appointments__title">APPOINTMENTS</h1>
  <div class="appointments__row">
    <span class="appointments__field">Date</span><span class="appointments__dots appointments__dots--date"></span>
    <span class="appointments__field">Time</span><span class="appointments__dots appointments__dots--time"></span>
  </div>
  <div class="appointments__row">
    <span class="appointments__field">Date</span><span class="appointments__dots appointments__dots--date"></span>
    <span class="appointments__field">Time</span><span class="appointments__dots appointments__dots--time"></span>
  </div>
  <div class="appointments__row">
    <span class="appointments__field">Date</span><span class="appointments__dots appointments__dots--date"></span>
    <span class="appointments__field">Time</span><span class="appointments__dots appointments__dots--time"></span>
  </div>
  <p class="appointments__note">If you are unable to keep your appointment,<br>please contact us as soon as possible.</p>
</section>

<section class="card card--front card--front-a">
  <div class="brand"><span class="brand__dot"></span><span class="brand__name">Dr Mei Lin Tan</span></div>
  <div class="card__divider"></div>
  <div class="details">
    <div class="details__name">Mei Lin Tan</div>
    <div class="details__credentials">MD FRCSC FRACS</div>
    <div class="details__specialty">Endocrine and General Surgeon</div>
    <div class="details__contact">
      T: (08) 5550 2481<br>
      F: (08) 5550 7316<br>
      E: info@drmeilintan.au
    </div>
    <div class="details__address">
      Suite 12, Level 3,<br>
      Harbourview Medical Centre<br>
      8 Linden Grove Parade,<br>
      Kestrel Bay, WA 6999<br>
      www.coastendocrinesurgeon.com.au
    </div>
  </div>
</section>

<section class="card card--front card--front-b">
  <div class="brand"><span class="brand__dot"></span><span class="brand__name">Dr Mei Lin Tan</span></div>
  <div class="card__divider"></div>
  <div class="details">
    <div class="details__name">Mei Lin Tan</div>
    <div class="details__credentials">MD FRCSC FRACS</div>
    <div class="details__specialty">Endocrine and General Surgeon</div>
    <div class="details__contact">
      T: (08) 5550 2481<br>
      F: (08) 5550 7316<br>
      E: info@drmeilintan.au
    </div>
    <div class="details__address">
      Eastvale Medical Specialists<br>
      Suite 4, Level 2/45 Orchard Rd,<br>
      Eastvale WA 6998<br>
      www.coastendocrinesurgeon.com.au
    </div>
  </div>
</section>

</body>
</html>
```